Emerging Education Provider Needs a Contemporary and Compelling Promotional Presentation

We are Juniper Learning and Skills Institute, a privately owned institution that is really going places. We offer a range of Diploma, Language and Short courses for both Domestic and International students with both face to face delivery and on-line or blended. We currently run out of two campuses in Brisbane (Queensland Australia) one in the heart of the city and one in the multi-cultural precinct of Bellhaven Rise. We are currently expanding with additional campuses planned for the Gold Coast and for Melbourne, Victoria.
Please refer to our web site jlsi-example.edu.au.
We need a promotional presentation (doesn't necessarily have to be in PowerPoint) to promote our business - It really needs to pop!
Proposed Pack:
Opening slide
Content & Agenda
CEO Welcome
Mission and Vision
Our Values
Why Choose JLSI (multiple slides)
Our Campuses (Brisbane, Bellhaven Rise, In Development)
Life in Brisbane (2 slides - Queensland and Brisbane)
Our Courses (3 slides - Domestic, International, On-Line)
Student Services (multiple slides)
How to Apply
Closing Slide
Updates

Reason: I will be travelling and unable to review submissions until early next week. Can all submissions please ensure the pack has a real wow factor. This will be a pack that we will have on a big screen at a trade show where thousands of people are walking by. The presentation needs to get people to stop and watch. So no graphs or data, few words per slide, lots of compelling images, a real contemporary feel.

Target Market(s)

Educational institutions, prospective students, Business to Business, seminars and trade shows.

Industry/Entity Type

Education

Font styles to use
Sans Serif

Colors
a54499

Requirements
Must have
• Consistent with our branding theme / colours.
• Template + content using information from our International Prospectus and web site.
• Delineation between domestic and international offerings.
• Showcasing the beautiful location from which we operate.
Nice to have
• Ability to utilise the presentation for generation of other marketing collateral (flyers, posters) in future.
• Cut in video footage of our location (Queensland, Brisbane, Gold Coast).
• Any general content / slides / video that may inspire travel to Australia to study or participation in study.
Should not have
• Be off-brand.

```html
<!DOCTYPE html>
<html lang="en">
<head>
<meta charset="utf-8">
<title>JLSI Presentation Pack</title>
<link href="https://fonts.googleapis.com/css2?family=Oswald:wght@400;500&family=Open+Sans:wght@400;600;700&display=swap" rel="stylesheet">
<style>
:root{
  --brand:#a54499;
  --brand-dark:#8a3580;
  --brand-soft:#c58bbd;
  --stage:#4b4b4b;
  --paper:#ffffff;
  --ink:#333333;
  --muted:#777777;
  --line:#d8d8d8;
  --photo-cool:#7d93ad;
  --photo-warm:#a88f78;
  --photo-dark:#3d4350;
}
*{box-sizing:border-box;margin:0;padding:0}
html,body{width:1200px;height:1157px;overflow:hidden}
body{background:var(--stage);font-family:"Open Sans",Arial,sans-serif;color:var(--ink);position:relative}
.slide{position:absolute;width:318px;height:179px;background:var(--paper);overflow:hidden}
.abs{position:absolute}
.photo{position:absolute;background:linear-gradient(135deg,var(--photo-cool),var(--photo-dark))}
.photo.warm{background:linear-gradient(135deg,var(--photo-warm),#5b4a3e)}
.photo.sky{background:linear-gradient(180deg,#b9d2ea,#5d7898 60%,#39465a)}
.photo.green{background:linear-gradient(160deg,#8aa36a,#4d6a44)}
.photo.night{background:linear-gradient(135deg,#1d2230,#5a4a5a)}
.heading{position:absolute;left:18px;top:14px;font-size:6.6px;font-weight:700;letter-spacing:.2px;text-transform:uppercase}
.heading::after{content:"";display:block;width:18px;height:1.5px;background:var(--brand);margin-top:3px}
.body-text{font-size:3.4px;line-height:1.45;color:var(--muted);text-align:justify}
.pg{position:absolute;right:6px;bottom:4px;font-size:3px;color:#aaa}
.condensed{font-family:"Oswald",Arial,sans-serif}
.purple{color:var(--brand)}
/* cover */
.logo-name{font-family:"Open Sans",Arial,sans-serif;font-weight:700;font-size:15px;color:#222;display:flex;align-items:center;gap:4px}
.logo-name i{display:inline-block;width:8px;height:8px;background:#222}
.cover-title{font-family:"Oswald",Arial,sans-serif;font-size:15px;line-height:1.25;text-transform:uppercase}
/* agenda */
.agenda-item{position:absolute;left:16px;display:flex;align-items:center;gap:6px;font-size:3.8px}
.agenda-item b{width:7px;height:7px;background:var(--brand);color:#fff;font-size:4px;display:flex;align-items:center;justify-content:center;font-weight:600}
/* cards */
.svc-box{position:absolute;width:64px;height:34px;border:1px solid #555;background:#fff;padding:6px 4px 0;text-align:center}
.svc-box.accent{border-color:var(--brand)}
.svc-box h4{font-size:4.2px;font-weight:700}
.svc-box.accent h4{color:var(--brand)}
.svc-box p{font-size:2.6px;line-height:1.4;color:var(--muted)}
.svc-badge{position:absolute;top:-6px;right:4px;width:15px;height:9px;background:#555}
.svc-box.accent .svc-badge{background:var(--brand)}
.icon-cell{position:absolute;width:56px;text-align:center}
.icon-cell h4{font-size:4.2px;font-weight:600;margin:3px 0 2px}
.icon-cell p{font-size:2.6px;line-height:1.4;color:var(--muted)}
.col-card{position:absolute;top:42px;width:41px;height:102px}
.col-card .photo{left:0;top:0;width:41px;height:50px}
.col-card .tag{position:absolute;top:50px;left:0;width:41px;height:7px;color:#fff;font-size:3.4px;font-weight:600;text-align:center;line-height:7px}
.col-card ul{position:absolute;top:57px;left:0;width:41px;height:45px;list-style:none;padding:3px 3px;font-size:2.5px;line-height:1.6;color:#fff}
.col-card.p .tag,.col-card.p ul{background:var(--brand)}
.col-card.d .tag,.col-card.d ul{background:#3c3c3c}
.campus-label{position:absolute;left:13px;bottom:-2px;width:101px;height:32px;background:var(--brand);color:#fff;text-align:center}
.campus-label h5{font-size:6px;font-weight:600;margin-top:5px}
.campus-label p{font-size:2.8px;line-height:1.4;margin-top:2px}
</style>
</head>
<body>

<!-- 1 Cover -->
<section class="slide" style="left:94px;top:84px">
  <div class="abs logo-name" style="left:22px;top:18px"><i></i>JLSI</div>
  <div class="abs cover-title" style="left:29px;top:86px">Edit Head<br><span class="purple">Title Here</span></div>
  <div class="photo warm" style="left:110px;top:0;width:208px;height:179px" role="img" aria-label="Two students looking at a notice board"></div>
</section>

<!-- 2 Agenda -->
<section class="slide" style="left:428px;top:84px">
  <div class="heading" style="left:25px;top:17px">Content &amp; Agenda</div>
  <div class="agenda-item" style="top:52px"><b>1</b>Lorem ipsum dolor sit amet, ur</div>
  <div class="agenda-item" style="top:75px"><b>2</b>Lorem ipsum dolor sit amet, ur</div>
  <div class="agenda-item" style="top:98px"><b>3</b>Lorem ipsum dolor sit amet, ur</div>
  <div class="agenda-item" style="top:121px"><b>4</b>Lorem ipsum dolor sit amet, ur</div>
  <div class="agenda-item" style="top:144px"><b>5</b>Lorem ipsum dolor sit amet, ur</div>
  <div class="photo sky" style="left:128px;top:0;width:190px;height:179px" role="img" aria-label="Modern glass office tower against a blue sky"></div>
</section>

<!-- 3 CEO -->
<section class="slide" style="left:764px;top:84px">
  <div class="abs" style="left:0;top:0;width:125px;height:179px;background:var(--brand)"></div>
  <div class="photo" style="left:35px;top:40px;width:54px;height:54px;border-radius:50%;border:2px solid #fff;background:linear-gradient(135deg,#c9a77f,#6b5140)" role="img" aria-label="Portrait of the chief executive"></div>
  <div class="abs condensed" style="left:0;width:125px;top:99px;text-align:center;color:#fff;font-size:8px">MARA ELLISON<br><span style="font-size:5px">CEO</span></div>
  <div class="heading" style="left:143px;top:22px">CEO Welcome</div>
  <div class="abs body-text" style="left:146px;top:48px;width:160px">Lorem ipsum dolor sit amet consectetur adipiscing elit. Cras bibendum mattis leo, ac efficitur ipsum lobortis non. Praesent vitae pulvinar metus. Phasellus accumsan elementum condimentum. Nullam rutrum, tellus tincidunt scelerisque placerat, justo lectus luctus odio, varius auctor urna lacus sed nisl.<br><br>Amet consectetur adipiscing elit. Cras bibendum mattis leo, ac efficitur ipsum lobortis non. Praesent vitae pulvinar metus. Phasellus accumsan elementum condimentum. Nullam rutrum, tellus tincidunt scelerisque placerat, justo lectus luctus odio, varius auctor urna lacus sed nisl. Suspendisse at placerat sem. Duis tincidunt augue vel eros hendrerit tempus. Lorem ipsum dolor sit amet consectetur adipiscing elit. Nullam rutrum tellus.</div>
  <div class="pg">3</div>
</section>

<!-- 4 Mission -->
<section class="slide" style="left:94px;top:280px;background:linear-gradient(180deg,#b86aae,#8d4785 60%,#a8609e)" role="img" aria-label="Hilltop landscape with a wind turbine in purple tones">
  <div class="abs condensed" style="left:27px;top:62px;color:#fff;font-size:13px;line-height:1.45;font-family:'Open Sans',Arial,sans-serif;font-weight:400">MISSION<br>AND<br>VISION</div>
  <div class="abs" style="left:109px;top:30px;width:209px;height:120px;background:#fff"></div>
  <div class="abs" style="left:214px;top:45px;width:1px;height:90px;background:var(--line)"></div>
  <div class="abs" style="left:128px;top:47px;width:75px"><div style="font-size:4.4px;font-weight:600;margin-bottom:4px">MISSION</div><div class="body-text">Lorem ipsum dolor sit amet, consectetur adipiscing elit, sed do eiusmod tempor incididunt ut labore et dolore magna aliqua. Ut enim ad minim veniam, quis nostrud exercitation ullamco laboris nisi ut aliquip ex ea commodo consequat. Duis aute irure dolor in reprehenderit in voluptate velit esse cillum dolore eu fugiat nulla pariatur.</div></div>
  <div class="abs" style="left:227px;top:47px;width:75px"><div style="font-size:4.4px;font-weight:600;margin-bottom:4px">VISION</div><div class="body-text">Lorem ipsum dolor sit amet, consectetur adipiscing elit, sed do eiusmod tempor incididunt ut labore et dolore magna aliqua. Ut enim ad minim veniam, quis nostrud exercitation ullamco laboris nisi ut aliquip ex ea commodo consequat. Duis aute irure dolor in reprehenderit in voluptate velit esse cillum dolore eu fugiat nulla pariatur.</div></div>
</section>

<!-- 5 Values -->
<section class="slide" style="left:428px;top:280px">
  <div class="heading">Our Values</div>
  <div class="photo night" style="left:18px;top:36px;width:120px;height:126px" role="img" aria-label="Woman holding a glowing heart of lights"></div>
  <div class="abs body-text" style="left:155px;top:42px;width:148px;text-align:center">Lorem ipsum dolor sit amet, consectetur adipiscing elit, sed do eiusmod tempor incididunt ut labore et dolore magna aliqua. Ut enim ad minim veniam, quis nostrud exercitation ullamco laboris nisi ut aliquip ex ea commodo consequat. Duis aute irure dolor in reprehenderit in voluptate velit esse cillum dolore eu fugiat nulla pariatur. Excepteur sint occaecat cupidatat non proident.</div>
  <svg class="abs" style="left:166px;top:108px" width="130" height="16" viewBox="0 0 130 16">
    <g fill="none" stroke="#a54499" stroke-width="1.2">
      <rect x="4" y="2" width="12" height="12"/><path d="M7 9l3-3 3 3M10 6v6"/>
      <path d="M56 14h14M58 12V9M62 12V6M66 12V4M58 8l4-3 4-2"/>
      <rect x="108" y="2" width="9" height="12"/><rect x="117" y="6" width="6" height="8"/><path d="M110 5h5M110 8h5M110 11h5"/>
    </g>
  </svg>
  <div class="abs body-text" style="left:155px;top:130px;width:48px;text-align:center;font-size:2.6px">Lorem ipsum dolor sit amet, consectetur adipiscing elit, sed do eiusmod tempor</div>
  <div class="abs body-text" style="left:207px;top:130px;width:48px;text-align:center;font-size:2.6px">Lorem ipsum dolor sit amet, consectetur adipiscing elit, sed do eiusmod tempor</div>
  <div class="abs body-text" style="left:259px;top:130px;width:48px;text-align:center;font-size:2.6px">Lorem ipsum dolor sit amet, consectetur adipiscing elit, sed do eiusmod tempor</div>
  <div class="pg">5</div>
</section>

<!-- 6 Why choose -->
<section class="slide" style="left:764px;top:280px">
  <div class="heading">Why Choose JLSI</div>
  <div class="abs body-text" style="left:20px;top:34px;width:145px">Lorem ipsum dolor sit amet consectetur adipiscing elit. Cras bibendum mattis leo, ac efficitur ipsum lobortis non. Praesent vitae pulvinar metus. Phasellus accumsan elementum condimentum. Nullam rutrum, tellus tincidunt scelerisque placerat, justo lectus luctus odio, varius auctor urna lacus sed nisl. Suspendisse at placerat sem. Duis tincidunt augue vel eros hendrerit tempus.<br><br>Amet consectetur adipiscing elit. Cras bibendum mattis leo, ac efficitur ipsum lobortis non. Praesent vitae pulvinar metus. Phasellus accumsan elementum condimentum. Nullam rutrum, tellus tincidunt scelerisque placerat, justo lectus luctus odio, varius auctor urna lacus sed nisl. Suspendisse at placerat sem. Duis tincidunt augue vel eros hendrerit tempus. Lorem ipsum dolor sit amet consectetur adipiscing elit. Cras bibendum mattis leo, ac efficitur ipsum lobortis non.</div>
  <div class="photo" style="left:173px;top:36px;width:64px;height:42px" role="img" aria-label="Man working at a computer"></div>
  <div class="photo sky" style="left:242px;top:36px;width:55px;height:50px" role="img" aria-label="Student at a laptop"></div>
  <div class="photo warm" style="left:195px;top:83px;width:42px;height:52px" role="img" aria-label="Hands writing notes"></div>
  <div class="photo" style="left:242px;top:92px;width:55px;height:66px" role="img" aria-label="Colleagues in a meeting"></div>
  <div class="pg">6</div>
</section>

<!-- 7 Campuses -->
<section class="slide" style="left:94px;top:478px">
  <div class="heading">Our Campuses</div>
  <div class="photo sky" style="left:27px;top:38px;width:126px;height:127px" role="img" aria-label="Heritage city campus building"></div>
  <div class="campus-label" style="left:40px;bottom:14px"><h5>JLSI City</h5><p>Level 4, 52 Wattle Lane, Brisbane CBD, QLD<br>4000, Australia</p></div>
  <div class="photo warm" style="left:166px;top:38px;width:126px;height:127px" role="img" aria-label="Brick campus building"></div>
  <div class="campus-label" style="left:179px;bottom:14px"><h5>JLSI Bellhaven</h5><p>210 Orchard Road, Bellhaven Rise,<br>QLD 4122, Australia</p></div>
  <div class="pg">7</div>
</section>

<!-- 8 Brisbane -->
<section class="slide" style="left:428px;top:478px">
  <div class="heading">Life in Brisbane</div>
  <div class="abs purple" style="left:20px;top:38px;width:92px;text-align:right;font-size:6px;font-weight:600">Queensland</div>
  <div class="abs body-text" style="left:29px;top:50px;width:84px;text-align:center">Lorem ipsum dolor sit amet consectetur adipiscing elit. Cras bibendum mattis leo, ac efficitur ipsum lobortis non. Praesent vitae pulvinar metus. Phasellus accumsan elementum condimentum. Nullam rutrum, tellus tincidunt scelerisque placerat, justo lectus luctus odio, varius auctor urna lacus sed nisl. Suspendisse at placerat sem. Duis tincidunt augue vel eros hendrerit tempus. Lorem ipsum dolor sit amet consectetur adipiscing elit. Cras bibendum mattis leo, ac efficitur ipsum lobortis non. Praesent vitae pulvinar metus. Phasellus accumsan.</div>
  <div class="photo sky" style="left:127px;top:16px;width:92px;height:149px" role="img" aria-label="Aerial view of the city and river"></div>
  <div class="photo green" style="left:223px;top:16px;width:81px;height:92px" role="img" aria-label="Riverside parkland"></div>
  <div class="photo warm" style="left:223px;top:112px;width:81px;height:53px" role="img" aria-label="Busy street market"></div>
  <div class="pg">8</div>
</section>

<!-- 9 Courses -->
<section class="slide" style="left:764px;top:478px">
  <div class="heading" style="top:11px">Our Courses</div>
  <div class="photo" style="left:0;top:33px;width:318px;height:130px;background:linear-gradient(90deg,var(--brand) 0%,var(--brand) 60%,#c9ccd3 61%,#9aa1ad)" role="img" aria-label="Students in a bright study space"></div>
  <div class="abs" style="left:12px;top:58px;width:70px;color:#fff;font-size:4.6px;font-weight:600;text-align:center;line-height:1.35">Lorem ipsum dolor sit amet consectetur adipiscing elit. Cras bibendum mattis leo, ac efficitur ipsum lobortis non. Praesent vitae pulvinar Lorem ipsum dolor sit amet consectetur adipiscing elit. Cras bibendum mattis leo.</div>
  <div class="abs" style="left:90px;top:52px;width:212px;height:105px;background:#fff"></div>
  <svg class="abs" style="left:120px;top:65px" width="160" height="14" viewBox="0 0 160 14">
    <g fill="#a54499"><path d="M0 5l8-4 8 4-8 4z"/><rect x="4" y="7" width="8" height="4"/>
    <rect x="61" y="1" width="16" height="12" fill="none" stroke="#a54499" stroke-width="1.3"/><circle cx="66" cy="6" r="2"/><rect x="69" y="5" width="6" height="1.2"/>
    <circle cx="134" cy="7" r="6"/></g>
  </svg>
  <div class="abs" style="left:104px;top:86px;width:60px;text-align:center"><div style="font-size:3.8px;font-weight:600;margin-bottom:3px">DIPLOMA</div><div class="body-text" style="text-align:center;font-size:2.6px">Lorem ipsum dolor sit amet consectetur adipiscing elit. Cras bibendum mattis leo, ac efficitur ipsum lobortis non. Praesent vitae pulvinar metus. Phasellus accumsan elementum condimentum.</div></div>
  <div class="abs" style="left:166px;top:86px;width:60px;text-align:center"><div style="font-size:3.8px;font-weight:600;margin-bottom:3px">CERTIFICATE</div><div class="body-text" style="text-align:center;font-size:2.6px">Lorem ipsum dolor sit amet consectetur adipiscing elit. Cras bibendum mattis leo, ac efficitur ipsum lobortis non. Praesent vitae pulvinar metus. Phasellus accumsan elementum condimentum.</div></div>
  <div class="abs" style="left:232px;top:86px;width:62px;text-align:center"><div style="font-size:3.8px;font-weight:600;margin-bottom:3px">INTERNATIONAL</div><div class="body-text" style="text-align:center;font-size:2.6px">Lorem ipsum dolor sit amet consectetur adipiscing elit. Cras bibendum mattis leo, ac efficitur ipsum lobortis non. Praesent vitae pulvinar metus. Phasellus accumsan elementum condimentum.</div></div>
  <div class="pg">10</div>
</section>

<!-- 10 Services boxes -->
<section class="slide" style="left:94px;top:676px">
  <div class="heading">Student Services</div>
  <div class="svc-box accent" style="left:24px;top:57px"><span class="svc-badge"></span><h4>LOREM IPSUM</h4><p>Lorem ipsum dolor sit amet, consectetur adipiscing elit. Aenean sed tempor lorem.</p></div>
  <div class="svc-box" style="left:94px;top:57px"><span class="svc-badge"></span><h4>LOREM IPSUM</h4><p>Lorem ipsum dolor sit amet, consectetur adipiscing elit. Aenean sed tempor lorem.</p></div>
  <div class="svc-box accent" style="left:163px;top:57px"><span class="svc-badge"></span><h4>LOREM IPSUM</h4><p>Lorem ipsum dolor sit amet, consectetur adipiscing elit. Aenean sed tempor lorem.</p></div>
  <div class="svc-box" style="left:233px;top:57px"><span class="svc-badge"></span><h4>LOREM IPSUM</h4><p>Lorem ipsum dolor sit amet, consectetur adipiscing elit. Aenean sed tempor lorem.</p></div>
  <div class="svc-box" style="left:24px;top:104px"><span class="svc-badge"></span><h4>LOREM IPSUM</h4><p>Lorem ipsum dolor sit amet, consectetur adipiscing elit. Aenean sed tempor lorem.</p></div>
  <div class="svc-box accent" style="left:94px;top:104px"><span class="svc-badge"></span><h4>LOREM IPSUM</h4><p>Lorem ipsum dolor sit amet, consectetur adipiscing elit. Aenean sed tempor lorem.</p></div>
  <div class="svc-box" style="left:163px;top:104px"><span class="svc-badge"></span><h4>LOREM IPSUM</h4><p>Lorem ipsum dolor sit amet, consectetur adipiscing elit. Aenean sed tempor lorem.</p></div>
  <div class="svc-box accent" style="left:233px;top:104px"><span class="svc-badge"></span><h4>LOREM IPSUM</h4><p>Lorem ipsum dolor sit amet, consectetur adipiscing elit. Aenean sed tempor lorem.</p></div>
  <div class="pg">11</div>
</section>

<!-- 11 Services icons -->
<section class="slide" style="left:428px;top:676px">
  <div class="heading">Student Services</div>
  <svg class="abs" style="left:0;top:44px" width="318" height="80" viewBox="0 0 318 80">
    <g fill="none" stroke="#a54499" stroke-width="1.3">
      <circle cx="50" cy="5" r="4"/><circle cx="104" cy="5" r="4.5"/><path d="M152 9h12M154 9V3M158 9V3M162 9V3M152 2.5l6-2.5 6 2.5"/>
      <ellipse cx="212" cy="5" rx="5" ry="3.5"/><rect x="261" y="1" width="11" height="8"/><path d="M261 1l5.5 4 5.5-4"/>
      <circle cx="49" cy="65" r="4.5"/><path d="M49 62v3h2"/><circle cx="104" cy="65" r="3"/><rect x="155" y="62" width="10" height="7"/><circle cx="160" cy="65.5" r="2"/>
      <path d="M207 69h10v-7M209 66l3 2 5-6"/><path d="M266 60v7M263 64l3 3 3-3M261 70h10"/>
    </g>
  </svg>
  <div class="icon-cell" style="left:22px;top:52px"><h4>LOREM IPSUM</h4><p>Lorem ipsum dolor sit amet, consectetur adipiscing elit, sed do eiusmod tempor incididunt ut lab</p></div>
  <div class="icon-cell" style="left:77px;top:52px"><h4>LOREM IPSUM</h4><p>Lorem ipsum dolor sit amet, consectetur adipiscing elit, sed do eiusmod tempor incididunt ut lab</p></div>
  <div class="icon-cell" style="left:132px;top:52px"><h4>LOREM IPSUM</h4><p>Lorem ipsum dolor sit amet, consectetur adipiscing elit, sed do eiusmod tempor incididunt ut lab</p></div>
  <div class="icon-cell" style="left:186px;top:52px"><h4>LOREM IPSUM</h4><p>Lorem ipsum dolor sit amet, consectetur adipiscing elit, sed do eiusmod tempor incididunt ut lab</p></div>
  <div class="icon-cell" style="left:240px;top:52px"><h4>LOREM IPSUM</h4><p>Lorem ipsum dolor sit amet, consectetur adipiscing elit, sed do eiusmod tempor incididunt ut lab</p></div>
  <div class="icon-cell" style="left:22px;top:112px"><h4>LOREM IPSUM</h4><p>Lorem ipsum dolor sit amet, consectetur adipiscing elit, sed do eiusmod tempor incididunt ut lab</p></div>
  <div class="icon-cell" style="left:77px;top:112px"><h4>LOREM IPSUM</h4><p>Lorem ipsum dolor sit amet, consectetur adipiscing elit, sed do eiusmod tempor incididunt ut lab</p></div>
  <div class="icon-cell" style="left:132px;top:112px"><h4>LOREM IPSUM</h4><p>Lorem ipsum dolor sit amet, consectetur adipiscing elit, sed do eiusmod tempor incididunt ut lab</p></div>
  <div class="icon-cell" style="left:186px;top:112px"><h4>LOREM IPSUM</h4><p>Lorem ipsum dolor sit amet, consectetur adipiscing elit, sed do eiusmod tempor incididunt ut lab</p></div>
  <div class="icon-cell" style="left:240px;top:112px"><h4>LOREM IPSUM</h4><p>Lorem ipsum dolor sit amet, consectetur adipiscing elit, sed do eiusmod tempor incididunt ut lab</p></div>
  <div class="pg">12</div>
</section>

<!-- 12 Services columns -->
<section class="slide" style="left:764px;top:676px">
  <div class="heading">Student Services</div>
  <div class="col-card p" style="left:18px"><div class="photo" role="img" aria-label="Business meeting scene"></div><div class="tag">SERVICES</div><ul><li>• Lorem ipsum dolor</li><li>• Lorem ipsum dolor</li><li>• Lorem ipsum dolor</li><li>• Lorem ipsum dolor</li><li>• Lorem ipsum dolor</li><li>• Lorem ipsum dolor</li></ul></div>
  <div class="col-card d" style="left:65px"><div class="photo warm" role="img" aria-label="Pocket watch close-up"></div><div class="tag">SERVICES</div><ul><li>• Lorem ipsum dolor</li><li>• Lorem ipsum dolor</li><li>• Lorem ipsum dolor</li><li>• Lorem ipsum dolor</li><li>• Lorem ipsum dolor</li><li>• Lorem ipsum dolor</li></ul></div>
  <div class="col-card p" style="left:112px"><div class="photo sky" role="img" aria-label="Team in an office"></div><div class="tag">SERVICES</div><ul><li>• Lorem ipsum dolor</li><li>• Lorem ipsum dolor</li><li>• Lorem ipsum dolor</li><li>• Lorem ipsum dolor</li><li>• Lorem ipsum dolor</li><li>• Lorem ipsum dolor</li></ul></div>
  <div class="col-card d" style="left:159px"><div class="photo" role="img" aria-label="Staff member at a desk"></div><div class="tag">SERVICES</div><ul><li>• Lorem ipsum dolor</li><li>• Lorem ipsum dolor</li><li>• Lorem ipsum dolor</li><li>• Lorem ipsum dolor</li><li>• Lorem ipsum dolor</li><li>• Lorem ipsum dolor</li></ul></div>
  <div class="col-card p" style="left:206px"><div class="photo sky" role="img" aria-label="Computer screens"></div><div class="tag">SERVICES</div><ul><li>• Lorem ipsum dolor</li><li>• Lorem ipsum dolor</li><li>• Lorem ipsum dolor</li><li>• Lorem ipsum dolor</li><li>• Lorem ipsum dolor</li><li>• Lorem ipsum dolor</li></ul></div>
  <div class="col-card d" style="left:253px"><div class="photo" role="img" aria-label="Group discussion"></div><div class="tag">SERVICES</div><ul><li>• Lorem ipsum dolor</li><li>• Lorem ipsum dolor</li><li>• Lorem ipsum dolor</li><li>• Lorem ipsum dolor</li><li>• Lorem ipsum dolor</li><li>• Lorem ipsum dolor</li></ul></div>
  <div class="pg">13</div>
</section>

<!-- 13 How to apply -->
<section class="slide" style="left:94px;top:872px">
  <div class="heading">How to Apply</div>
  <div class="abs" style="left:0;top:140px;width:318px;height:20px;background:var(--brand)"></div>
  <div class="photo" style="left:15px;top:33px;width:125px;height:146px;background:linear-gradient(135deg,#e9e6e2,#a7a9ad)" role="img" aria-label="Hands typing on a laptop"></div>
  <div class="abs" style="left:152px;top:38px;width:155px;font-size:3.6px;line-height:1.5">
    <b style="font-size:3.6px">Lorem ipsum dolor:</b>
    <ul style="margin:6px 0 6px 8px;color:var(--muted)"><li>Lorem ipsum dolor sit amet</li><li>consectetur adipiscing elit</li><li>Cras bibendum mattis leo, ac</li><li>efficitur ipsum lobortis non</li></ul>
    <b>Lorem ipsum dolor:</b>
    <div class="body-text" style="margin-top:5px">Lorem ipsum dolor sit amet consectetur adipiscing elit. Cras bibendum mattis leo, ac efficitur ipsum lobortis non. Praesent vitae pulvinar metus. Phasellus accumsan elementum condimentum. Nullam rutrum, tellus tincidunt scelerisque placerat, justo lectus luctus odio, varius auctor urna lacus sed nisl. Suspendisse at placerat sem. Lorem ipsum dolor sit amet consectetur adipiscing elit.</div>
  </div>
  <div class="abs" style="left:158px;top:146px;color:#fff;font-size:4.6px">Lorem ipsum dolor sit amet consectetur adipiscing elit</div>
  <div class="pg">14</div>
</section>

<!-- 14 Edit title -->
<section class="slide" style="left:428px;top:872px">
  <div class="heading" style="top:15px">Edit Title Here</div>
  <div class="photo" style="left:29px;top:33px;width:83px;height:120px;background:linear-gradient(135deg,#8ba4c0,#2c3a52)" role="img" aria-label="Woman with a digital interface overlay"></div>
  <div class="abs condensed purple" style="left:129px;top:40px;font-size:8px">LOREM IPSUM</div>
  <div class="abs body-text" style="left:129px;top:55px;width:174px">Lorem ipsum dolor sit amet consectetur adipiscing elit. Cras bibendum mattis leo, ac efficitur ipsum lobortis non. Praesent vitae pulvinar metus. Phasellus accumsan elementum condimentum. Nullam rutrum, tellus tincidunt scelerisque placerat, justo lectus luctus odio, varius auctor urna lacus sed nisl. Suspendisse at placerat sem. Duis tincidunt augue vel eros hendrerit tempus. Lorem ipsum dolor sit amet consectetur adipiscing elit. Cras bibendum mattis leo, ac efficitur ipsum lobortis non. Praesent vitae pulvinar metus. Phasellus accumsan elementum condimentum. Nullam rutrum, tellus tincidunt scelerisque placerat, justo lectus luctus odio, varius auctor urna lacus sed nisl. Suspendisse at placerat sem. Duis tincidunt augue vel eros hendrerit tempus. Cras bibendum mattis leo, ac efficitur ipsum lobortis non. Praesent vitae pulvinar metus. Phasellus accumsan elementum condimentum.</div>
  <div class="pg">15</div>
</section>

<!-- 15 Thank you -->
<section class="slide" style="left:764px;top:872px">
  <div class="photo" style="left:0;top:0;width:318px;height:179px;background:linear-gradient(90deg,#c7a3b8,#d9c8bb 60%,#8c8577)" role="img" aria-label="Group of students working together at a table"></div>
  <div class="abs" style="left:28px;top:0;width:133px;height:179px;background:rgba(165,68,153,.92)"></div>
  <div class="abs" style="left:28px;width:133px;top:85px;text-align:center;color:#fff;font-size:10.5px">THANK <b>YOU</b></div>
</section>

</body>
</html>
```